Design a professional card box for our toothpaste product.

We need an experienced freelance to design a professional card box for our toothpaste product.
Requirements:
1. Chinese font prefers Microsoft Yahei.
2. English fonts have no limitation.
3. The texts we required in the WORD document should occur in the relevant areas of card box.
At last, we hope that you could submit both 2D design and 3D visual effects.
Target Market(s)
orthodontic patients
Look and feel
Each slider illustrates characteristics of the customer's brand and the style your logo design should communicate.

```html
<!DOCTYPE html>
<html lang="en">
<head>
<meta charset="utf-8">
<title>Sparkle Surf M2300 Orthodontic Toothpaste – Carton Front Panel</title>
<link rel="stylesheet" href="https://fonts.googleapis.com/css2?family=Montserrat:wght@800&family=Oswald:wght@400&family=Roboto:ital,wght@1,400&family=Barlow:wght@400;500&display=swap">
<style>
  :root {
    --stage: #e6e7e9;
    --ocean: #2496de;
    --ice: #ffffff;
    --ink: #111111;
    --label-blue: #1a86d0;
    --claim-blue: #1c74bb;
    --spec-blue: #3fa5e6;
    --mint: #58b530;
    --mint-dark: #2f8a1e;
  }
  * { margin: 0; padding: 0; box-sizing: border-box; }
  html, body {
    width: 1200px;
    height: 1200px;
    overflow: hidden;
    background: var(--stage);
  }
  .carton-front {
    position: absolute;
    left: 50px;
    top: 455px;
    width: 1100px;
    height: 290px;
    overflow: hidden;
    background: linear-gradient(90deg, var(--ocean) 0%, #4fb0ea 22%, #b7def7 45%, var(--ice) 62%, var(--ice) 86%, #d5ecfb 100%);
  }
  .bubble-field {
    position: absolute;
    left: 0;
    top: 0;
    width: 620px;
    height: 290px;
    background:
      radial-gradient(circle at 150px 120px, rgba(255,255,255,0.35) 0 90px, transparent 92px),
      radial-gradient(circle at 300px 60px, rgba(255,255,255,0.18) 0 70px, transparent 72px),
      radial-gradient(circle at 200px 260px, rgba(255,255,255,0.22) 0 40px, transparent 42px);
  }
  .brand {
    position: absolute;
    left: 60px;
    top: 72px;
    display: flex;
    align-items: flex-end;
    gap: 8px;
  }
  .brand-name {
    font-family: "Montserrat", sans-serif;
    font-weight: 800;
    font-size: 48px;
    line-height: 50px;
    color: var(--ink);
  }
  .brand-dot {
    width: 14px;
    height: 14px;
    margin-bottom: 12px;
    border-radius: 50%;
    background: var(--ink);
  }
  .mint-leaf {
    position: absolute;
    left: 292px;
    top: 170px;
    width: 88px;
    height: 72px;
    border-radius: 50% 50% 45% 45%;
    background: radial-gradient(circle at 40% 40%, #8fd65a, var(--mint) 55%, var(--mint-dark));
  }
  .flavour {
    position: absolute;
    left: 314px;
    top: 246px;
    font-family: "Roboto", sans-serif;
    font-style: italic;
    font-size: 11px;
    color: var(--mint-dark);
    transform: rotate(-12deg);
  }
  .claims {
    position: absolute;
    right: 564px;
    top: 123px;
    text-align: right;
    font-family: "Roboto", sans-serif;
    font-style: italic;
    font-size: 13px;
    line-height: 14px;
    color: var(--claim-blue);
  }
  .product-type {
    position: absolute;
    right: 564px;
    top: 176px;
    text-align: right;
    font-family: "Oswald", sans-serif;
    font-weight: 400;
    font-size: 30px;
    line-height: 28px;
    color: var(--label-blue);
    transform: scaleX(0.82);
    transform-origin: right center;
  }
  .product-code {
    position: absolute;
    left: 550px;
    top: 92px;
    font-family: "Montserrat", sans-serif;
    font-weight: 800;
    font-size: 140px;
    line-height: 1;
    letter-spacing: -2px;
    color: var(--ink);
  }
  .net-weight {
    position: absolute;
    right: 44px;
    top: 25px;
    text-align: right;
    font-family: "Barlow", sans-serif;
    color: var(--label-blue);
  }
  .net-weight strong {
    display: block;
    font-weight: 500;
    font-size: 22px;
    line-height: 24px;
  }
  .net-weight span {
    display: block;
    font-weight: 400;
    font-size: 15px;
    color: var(--spec-blue);
  }
</style>
</head>
<body>
  <section class="carton-front">
    <div class="bubble-field" role="img" aria-label="Soft blue background of water bubbles and halftone dots"></div>

    <div class="brand">
      <div class="brand-name">Sparkle<br>Surf</div>
      <div class="brand-dot"></div>
    </div>

    <div class="mint-leaf" role="img" aria-label="Pair of fresh green mint leaves"></div>
    <div class="flavour">Double Mint</div>

    <p class="claims">Enhanced<br>Cavity Prevention<br>and Gum Protection</p>
    <p class="product-type">ORTHODONTIC<br>TOOTHPASTE</p>

    <div class="product-code">M2300</div>

    <div class="net-weight">
      <strong>NET WT. 85g</strong>
      <span>Fluoride 1450 ppm</span>
    </div>
  </section>
</body>
</html>
```